Brindlemoor Client Journey To Success

I need a one-page document that graphically shows the client's journey working with Brindlemoor from initial assessment to completed project. I want the journey to start at the "basecamp logo" and reach 4 summits (little mountain logos...) .

I'd like the imagery to convey the client starting at basecamp, and moving to each summit. Each summit, should list the subtext under each, as listed on the pdf doc i provided.

The description for the basecamp and 4 summits is attached.

I need the brochure to look like the other brochure that you did for me (attached) .

Target Market(s)

Restaurant Owners

Industry/Entity Type

Construction Management

Font styles to use
Sans Serif

Colors
EB3D1F
EC4F4E
F09395
F8D3D4
FCEDEE

Requirements
Must have
• My logo. Title: Client Journey To Success. Subtitle: The 4 Summits

```html
<!DOCTYPE html>
<html lang="en">
<head>
<meta charset="utf-8">
<title>Brindlemoor Development – Client Journey To Success</title>
<link rel="stylesheet" href="https://fonts.googleapis.com/css2?family=Montserrat:wght@500;600;700;800;900&family=Allura&family=Norican&display=swap">
<style>
  :root {
    --red: #e2231a;
    --red-bright: #eb3d1f;
    --red-deep: #a9151a;
    --ink: #161616;
    --text-grey: #555555;
    --panel-grey: #ebebeb;
    --paper: #ffffff;
  }
  * { box-sizing: border-box; margin: 0; padding: 0; }
  html, body { width: 973px; height: 1200px; overflow: hidden; background: var(--paper); }
  .flyer {
    position: relative; width: 973px; height: 1200px; overflow: hidden;
    background: var(--paper); font-family: "Montserrat", sans-serif; color: var(--text-grey);
  }
  .backdrop { position: absolute; inset: 0; width: 973px; height: 1200px; }
  .abs { position: absolute; line-height: 1; white-space: nowrap; }

  .brand-mark { left: 135px; top: 58px; width: 120px; height: 120px; border-radius: 50%; background: var(--red); }
  .brand-name { left: 46px; top: 248px; font-size: 20px; font-weight: 800; color: var(--ink); letter-spacing: 0.2px; }

  .services { left: 497px; top: 38px; list-style: none; }
  .services li {
    font-size: 20px; font-weight: 700; color: #4a4a4a; line-height: 27.5px;
    display: flex; align-items: center; gap: 7px;
  }
  .services li::before { content: ""; width: 11px; height: 11px; background: var(--red); border-radius: 50%; }

  .title-script { left: 486px; top: 262px; font-family: "Allura", cursive; font-size: 215px; color: var(--ink); }
  .title-line { font-size: 46px; font-weight: 900; color: var(--ink); letter-spacing: 0.5px; }
  .title-journey { left: 569px; top: 460px; }
  .title-success { left: 569px; top: 514px; }
  .title-success .accent { color: var(--red); }
  .subtitle-the { left: 314px; top: 584px; font-size: 28px; font-weight: 900; color: var(--ink); }
  .subtitle-script { left: 252px; top: 592px; font-family: "Norican", cursive; font-size: 74px; color: var(--ink); }

  .stage-title { font-size: 22px; font-weight: 800; color: var(--red); }
  .stage-sub { font-size: 13.5px; font-weight: 800; color: #3a3a3a; margin-top: 6px; }
  .stage-list { list-style: none; margin-top: 3px; }
  .stage-list li { font-size: 13.5px; font-weight: 600; color: var(--text-grey); line-height: 18.6px; }

  .basecamp { left: 255px; top: 711px; }
  .basecamp .stage-list { margin-top: 6px; }
  .basecamp .stage-list li { font-size: 16px; line-height: 20.5px; }

  .summit-1 { left: 301px; top: 861px; }
  .summit-3 { left: 639px; top: 861px; }
  .summit-2 { left: 301px; top: 1039px; }
  .summit-4 { left: 639px; top: 1039px; }

  .icon { position: absolute; width: 36px; height: 36px; }
  .icon-s1 { left: 252px; top: 852px; }
  .icon-s3 { left: 590px; top: 852px; }
  .icon-s2 { left: 252px; top: 1030px; }
  .icon-s4 { left: 590px; top: 1030px; }

  .contact-phone { left: 644px; top: 711px; font-size: 36px; font-weight: 800; color: var(--red); }
  .contact-line { font-size: 16px; font-weight: 600; color: var(--text-grey); }
  .contact-email { left: 646px; top: 756px; }
  .contact-web { left: 646px; top: 781px; }
  .contact-icon { position: absolute; }
</style>
</head>
<body>
<main class="flyer">
  <svg class="backdrop" viewBox="317 291 1107 1563" preserveAspectRatio="none" aria-hidden="true">
    <defs>
      <linearGradient id="band-red" x1="317" y1="0" x2="1424" y2="0" gradientUnits="userSpaceOnUse">
        <stop offset="0" stop-color="#e0241a"/>
        <stop offset="0.55" stop-color="#d01f1a"/>
        <stop offset="1" stop-color="#a9151a"/>
      </linearGradient>
    </defs>
    <polygon class="panel-grey" fill="#ebebeb"
      points="675,1165 1099,925 1424,1105 1424,1590 1016,1360 1016,1854 675,1854"/>
    <polygon fill="#ebebeb" points="1424,1690 1424,1854 1140,1854"/>
    <polygon class="chevron-band" fill="url(#band-red)"
      points="317,955 1099,505 1424,690 1424,908 1099,722 507,1060 507,1750 690,1854 317,1854"/>
    <g class="numeral-four" stroke="#e2231a" stroke-width="8" fill="none" stroke-linecap="square">
      <path d="M920,905 L772,1078 L983,1078"/>
      <path d="M920,1010 L920,1158"/>
    </g>
  </svg>

  <div class="abs brand-mark" aria-hidden="true"></div>
  <div class="abs brand-name">BRINDLEMOOR DEVELOPMENT</div>

  <ul class="abs services">
    <li>DESIGN</li>
    <li>PROGRAM MANAGEMENT</li>
    <li>PROJECT MANAGEMENT</li>
    <li>CONSTRUCTION MANAGEMENT</li>
  </ul>

  <h1>
    <span class="abs title-script">Client</span>
    <span class="abs title-line title-journey">JOURNEY</span>
    <span class="abs title-line title-success"><span class="accent">TO</span> SUCCESS</span>
  </h1>
  <h2>
    <span class="abs subtitle-the">THE</span>
    <span class="abs subtitle-script">Summits</span>
  </h2>

  <section class="abs basecamp">
    <h3 class="stage-title">Basecamp</h3>
    <ul class="stage-list">
      <li>a. Client Assessment</li>
      <li>b. Determine Project Goals</li>
      <li>c. Proposal &amp; Fees</li>
    </ul>
  </section>

  <svg class="contact-icon" style="left:593px;top:714px" width="24" height="24" viewBox="0 0 24 24" aria-hidden="true">
    <path fill="#161616" d="M6.6 10.8a15.1 15.1 0 0 0 6.6 6.6l2.2-2.2c.3-.3.7-.4 1-.2 1.1.4 2.3.6 3.6.6.6 0 1 .4 1 1V20c0 .6-.4 1-1 1A17 17 0 0 1 3 4c0-.6.4-1 1-1h3.5c.6 0 1 .4 1 1 0 1.3.2 2.5.6 3.6.1.3 0 .7-.2 1z"/>
  </svg>
  <div class="abs contact-phone">555-014-2287</div>

  <svg class="contact-icon" style="left:600px;top:757px" width="16" height="12" viewBox="0 0 16 12" aria-hidden="true">
    <rect x="0.5" y="0.5" width="15" height="11" fill="#e2231a"/>
    <path d="M1 1 L8 7 L15 1" stroke="#fff" stroke-width="1.3" fill="none"/>
  </svg>
  <div class="abs contact-line contact-email">team@brindlemoordevgroup.com</div>

  <svg class="contact-icon" style="left:600px;top:780px" width="16" height="16" viewBox="0 0 16 16" aria-hidden="true">
    <g stroke="#e2231a" stroke-width="1.3" fill="none">
      <circle cx="8" cy="8" r="7"/><ellipse cx="8" cy="8" rx="3" ry="7"/>
      <path d="M1 8h14M2.2 4.5h11.6M2.2 11.5h11.6"/>
    </g>
  </svg>
  <div class="abs contact-line contact-web">brindlemoordevgroup.com</div>

  <svg class="icon icon-s1" viewBox="0 0 36 36" aria-hidden="true">
    <g stroke="#e2231a" stroke-width="1.5" fill="none">
      <path d="M4 34h28M6 34V4M6 4h6v8H6M12 20h4v14M20 26a8 8 0 0 1 14 0v8"/>
      <circle cx="28" cy="8" r="4"/><path d="M22 34v-6h12"/>
    </g>
  </svg>
  <section class="abs summit-1">
    <h3 class="stage-title">Summit 1 -</h3>
    <p class="stage-sub">PreConstruction</p>
    <ul class="stage-list">
      <li>a. Develop Project Plan</li>
      <li>b. Develop Risk Assessment &amp; Plan</li>
      <li>c. Devlelop Schedule</li>
      <li>d. Develop Budget</li>
      <li>e. Develop Team</li>
      <li>f. GC, Sub, Consultants Contracts</li>
    </ul>
  </section>

  <svg class="icon icon-s3" viewBox="0 0 36 36" aria-hidden="true">
    <g stroke="#e2231a" stroke-width="1.5" fill="none">
      <path d="M18 4a10 10 0 0 0-6 18v5h12v-5a10 10 0 0 0-6-18z"/>
      <path d="M13 30h10M15 33h6"/><circle cx="18" cy="14" r="3.5"/>
    </g>
  </svg>
  <section class="abs summit-3">
    <h3 class="stage-title">Summit 3 -</h3>
    <p class="stage-sub">Project Management</p>
    <ul class="stage-list">
      <li>a. Shared Consciousness Meetings</li>
      <li>b. Pressurized Collaboration</li>
      <li>c. Schedule Management</li>
      <li>d. Run O.O.D.A. Loop</li>
    </ul>
  </section>

  <svg class="icon icon-s2" viewBox="0 0 36 36" aria-hidden="true">
    <g stroke="#e2231a" stroke-width="1.5" fill="none">
      <circle cx="18" cy="18" r="14" stroke-dasharray="4 2.5"/>
      <circle cx="18" cy="18" r="9"/><path d="M13.5 18l3 3 6-6"/>
    </g>
  </svg>
  <section class="abs summit-2">
    <h3 class="stage-title">Summit 2 -</h3>
    <p class="stage-sub">Execution</p>
    <ul class="stage-list">
      <li>a. Acquire Permits</li>
      <li>b. PreConstruction Meeting</li>
      <li>c. Project Start</li>
    </ul>
  </section>

  <svg class="icon icon-s4" viewBox="0 0 36 36" aria-hidden="true">
    <g stroke="#e2231a" stroke-width="1.5" fill="none">
      <rect x="5" y="6" width="22" height="27" rx="2"/><path d="M12 3h8v5h-8z"/>
      <path d="M9 14h3v3H9zM9 21h3v3H9zM15 15.5h8M15 22.5h6M24 32l9-9"/>
    </g>
  </svg>
  <section class="abs summit-4">
    <h3 class="stage-title">Summit 4 -</h3>
    <p class="stage-sub">Completion</p>
    <ul class="stage-list">
      <li>a. Closeout</li>
    </ul>
  </section>
</main>
</body>
</html>
```